Mortgage firm needs clean and simple wordpress website and logo

The competition is for design only, and the winning design for the homepage will be expected to create a second design for a simpler template for additional pages.

We need a logo and basic wordpress website design for a Sydney based mortgage firm.
We need a clean and simple logo and website, based on the mortgage/accounting/finance/tax industry. Simple, credible and official colors.

The logo is expected to be so simple that we have combined into the one job.
If you submit a logo design and we choose it along with someone else's website design you will be paid a bonus of $60. The website design will still win the competition as per normal.

Current website is old and terrible but gives you an idea of the sitemap (super simple) and what they do: http://www.loanharbourgroup.com.au/

We will integrate a mortgage calculator into the site.
The calculator is adjustable in styles, you can see it here: http://www.loanharbourgroup.com.au/mortgagecalculator/

We want original different to copy-and-paste template looking designs.
We like simple websites with a long home page and a few additional pages like https://www.homelendquest.com.au/

We are based in Sydney Australia and are mortgage brokers

We want a clean, formal, credible site, limited pages.

The project is guaranteed, so go for it.

Example of basic template after home page complete: http://loanharbourgroup.com.au/template_example.jpg

Target Market(s)

Mortgage and banking clients

Industry/Entity Type

Finance

Number of Pages Required

1 page

Requirements
Must have
• A simple logo, Wordpress capable, be able to incorporate the mortgage calculator (on the home page if needed as well as its own page)
Nice to have
• VIdeo - something free but nice

```html
<!DOCTYPE html>
<html lang="en">
<head>
<meta charset="utf-8">
<title>Loan Harbour Group — Private Funding</title>
<link href="https://fonts.googleapis.com/css2?family=Lato:wght@400;700&display=swap" rel="stylesheet">
<style>
  :root {
    --red: #d03a3a;
    --red-dark: #a82424;
    --ink: #4a4a4a;
    --muted: #8a8a8a;
    --card: #e6e6e6;
    --card-edge: #c8c8c8;
    --field-edge: #9a9a9a;
    --addon: #e4e4e4;
    --grid: #e2e2e2;
    --green: #00e600;
    --green-soft: #b7f2b7;
    --white: #ffffff;
  }
  * { box-sizing: border-box; margin: 0; padding: 0; }
  html, body { width: 768px; height: 1200px; overflow: hidden; background: var(--white); }
  body { position: relative; font-family: "Lato", Arial, sans-serif; color: var(--ink); }
  .abs { position: absolute; }

  .hero {
    left: 0; top: 0; width: 768px; height: 376px;
    background: linear-gradient(180deg, #3b4654 0%, #4d5866 45%, #5b6158 75%, #4a5a3e 100%);
  }
  .brand { left: 108px; top: 17px; display: flex; align-items: center; gap: 9px; color: var(--white); font-weight: 700; font-size: 18px; }
  .brand-mark { width: 38px; height: 30px; background: var(--red); }
  .contact-line { left: 404px; top: 7px; color: var(--white); font-size: 12px; font-weight: 700; word-spacing: 1px; }
  .contact-line span + span { margin-left: 22px; }
  .nav { left: 463px; top: 26px; display: flex; gap: 22px; font-size: 12.5px; font-weight: 700; color: var(--white); }
  .nav .current { color: var(--red); }

  .hero-title { left: 0; top: 138px; width: 768px; text-align: center; color: var(--white); font-size: 22px; font-weight: 700; line-height: 28px; }
  .hero-title em { font-style: normal; color: var(--red); }
  .hero-sub { left: 0; top: 206px; width: 768px; text-align: center; color: var(--white); font-size: 11.5px; line-height: 15px; }
  .cta {
    left: 312px; top: 267px; width: 144px; height: 36px; border-radius: 18px;
    background: linear-gradient(180deg, var(--red) 0%, var(--red-dark) 100%);
    color: var(--white); font-size: 15px; display: flex; align-items: center; justify-content: center;
    box-shadow: 0 2px 3px rgba(0,0,0,.35);
  }

  .feature { top: 318px; width: 181px; height: 201px; background: var(--card); border: 1px solid var(--card-edge); border-radius: 2px; padding: 6px 8px; }
  .feature h3 { font-size: 17px; font-weight: 700; color: #555; margin-bottom: 6px; }
  .feature p { font-size: 11px; line-height: 14px; color: var(--muted); }

  .calc-title { left: 0; top: 532px; width: 768px; text-align: center; font-size: 23px; font-weight: 700; color: #555; }
  .calc-title em, .result em { font-style: normal; color: var(--red); }
  .field-label { top: 571px; font-size: 11.5px; font-weight: 700; color: #555; text-align: center; }
  .field { top: 590px; height: 32px; display: flex; border: 1px solid var(--field-edge); background: var(--white); font-size: 11.5px; color: #555; }
  .field .addon { background: var(--addon); display: flex; align-items: center; justify-content: center; padding: 0 6px; }
  .field .addon.left { border-right: 1px solid var(--field-edge); width: 33px; }
  .field .addon.right { border-left: 1px solid var(--field-edge); }
  .field .value { flex: 1; }

  .result { left: 108px; top: 640px; font-size: 23px; font-weight: 700; color: #555; }

  .chart { left: 0; top: 690px; width: 768px; height: 280px; }
  .chart text { font-family: "Lato", Arial, sans-serif; font-weight: 700; fill: var(--muted); font-size: 12px; }
  .chart .stat-value { fill: #444; font-size: 13px; }
  .chart .tip-text { fill: #666; font-size: 12px; }

  .select-label { top: 976px; font-size: 11.5px; font-weight: 700; color: #555; text-align: center; }
  .select { top: 996px; height: 30px; display: flex; border: 1px solid var(--field-edge); background: var(--white); }
  .select .value { flex: 1; }
  .select .arrow { width: 44px; background: var(--addon); border-left: 1px solid var(--field-edge); display: flex; align-items: center; justify-content: center; }

  .footer { left: 0; top: 1048px; width: 768px; height: 152px; background: var(--red); color: var(--white); }
  .copyright { left: 108px; top: 1168px; font-size: 12.5px; color: var(--white); }
  .team { left: 532px; top: 1086px; width: 150px; font-size: 12.5px; line-height: 14px; color: var(--white); }
</style>
</head>
<body>
  <div class="abs hero" role="img" aria-label="Photo of a smiling couple standing in front of their new two-storey family home"></div>

  <div class="abs brand"><span class="brand-mark"></span>Loan Harbour Group</div>
  <div class="abs contact-line"><span>Phone +612 9400 1200</span><span>Fax +612 9400 1299</span></div>
  <nav class="abs nav"><span class="current">HOME</span><span>ABOUT</span><span>CONTACT US</span></nav>

  <h1 class="abs hero-title">Welcome To <em>Loan Harbour Group</em><br>Private Funding</h1>
  <p class="abs hero-sub">Home, investment and commercial loans for purchase, refinance and consolidation<br>at up to 80% lending.</p>
  <div class="abs cta">Contact Us Now</div>

  <section class="abs feature" style="left:111px">
    <h3>Experience</h3>
    <p>Loan Harbour Group have been organising and managing money for clients for over 25 years using our access to banks, private lenders and brokers within Australia.</p>
  </section>
  <section class="abs feature" style="left:294px">
    <h3>Fast</h3>
    <p>We can provide money in 24 Hours, providing you meet the loan criteria. Unlike banks that might take months to complete a loan, we can react to your demands quickly.</p>
  </section>
  <section class="abs feature" style="left:477px">
    <h3>Private</h3>
    <p>Our specialty is private lending for residential, commercial and industrial properties. We generally look for registered first mortgage security with up to 80% loan funding based on the property valuation, the type of security and the borrower profile.</p>
  </section>

  <h2 class="abs calc-title">Mortgage <em>Calculator</em></h2>
  <div class="abs field-label" style="left:110px;width:140px">Loan Amount</div>
  <div class="abs field-label" style="left:288px;width:140px">Loan Term</div>
  <div class="abs field-label" style="left:466px;width:139px">Loan Interest</div>
  <div class="abs field" style="left:110px;width:140px"><span class="addon left">$</span><span class="value"></span><span class="addon right">AUD</span></div>
  <div class="abs field" style="left:288px;width:140px"><span class="value"></span><span class="addon right">YEARS</span></div>
  <div class="abs field" style="left:466px;width:139px"><span class="value"></span><span class="addon right" style="width:36px">%</span></div>

  <h2 class="abs result">Your repayment would be <em>600 per month</em></h2>

  <svg class="abs chart" viewBox="0 690 768 280" aria-label="Principal remaining over the loan term">
    <g stroke="var(--grid)" stroke-width="1.5">
      <line x1="163" y1="716" x2="555" y2="716"/>
      <line x1="163" y1="771" x2="555" y2="771"/>
      <line x1="163" y1="826" x2="555" y2="826"/>
      <line x1="163" y1="880" x2="555" y2="880"/>
      <line x1="163" y1="934" x2="555" y2="934"/>
    </g>
    <g text-anchor="end">
      <text x="151" y="720">100,000</text>
      <text x="151" y="775">75,000</text>
      <text x="151" y="830">50,000</text>
      <text x="151" y="884">25,000</text>
      <text x="151" y="938">0</text>
    </g>
    <g text-anchor="middle">
      <text x="204" y="956">2020</text>
      <text x="335" y="956">2030</text>
      <text x="466" y="956">2040</text>
    </g>
    <polyline fill="none" stroke="var(--green)" stroke-width="3" points="163,716 176.1,718.6 189.1,721.2 202.2,724.1 215.3,727.1 228.4,730.4 241.4,733.9 254.5,737.6 267.6,741.5 280.6,745.6 293.7,750 306.8,754.8 319.8,759.8 332.9,765.3 346,770.9 359.1,777 372.1,783.6 385.2,790.3 398.3,797.8 411.3,805.6 424.4,814.1 437.5,822.8"/>
    <polyline fill="none" stroke="var(--green-soft)" stroke-width="3" points="437.5,822.8 450.5,832.4 463.6,842.4 476.7,853.1 489.8,864.7 502.8,876.9 515.9,889.7 529,903.7 542,918.3"/>
    <polyline fill="none" stroke="var(--green)" stroke-width="3" points="542,918.3 555,934"/>
    <g fill="var(--green)">
      <circle cx="163" cy="716" r="4"/><circle cx="176.1" cy="718.6" r="4"/><circle cx="189.1" cy="721.2" r="4"/><circle cx="202.2" cy="724.1" r="4"/><circle cx="215.3" cy="727.1" r="4"/><circle cx="228.4" cy="730.4" r="4"/><circle cx="241.4" cy="733.9" r="4"/><circle cx="254.5" cy="737.6" r="4"/><circle cx="267.6" cy="741.5" r="4"/><circle cx="280.6" cy="745.6" r="4"/><circle cx="293.7" cy="750" r="4"/><circle cx="306.8" cy="754.8" r="4"/><circle cx="319.8" cy="759.8" r="4"/><circle cx="332.9" cy="765.3" r="4"/><circle cx="346" cy="770.9" r="4"/><circle cx="359.1" cy="777" r="4"/><circle cx="372.1" cy="783.6" r="4"/><circle cx="385.2" cy="790.3" r="4"/><circle cx="398.3" cy="797.8" r="4"/><circle cx="411.3" cy="805.6" r="4"/><circle cx="424.4" cy="814.1" r="4"/><circle cx="437.5" cy="822.8" r="4"/>
      <circle cx="542" cy="918.3" r="7"/><circle cx="555" cy="934" r="4"/>
    </g>
    <g fill="var(--green-soft)">
      <circle cx="450.5" cy="832.4" r="4"/><circle cx="463.6" cy="842.4" r="4"/><circle cx="476.7" cy="853.1" r="4"/><circle cx="489.8" cy="864.7" r="4"/><circle cx="502.8" cy="876.9" r="4"/><circle cx="515.9" cy="889.7" r="4"/><circle cx="529" cy="903.7" r="4"/>
    </g>
    <rect x="444" y="821" width="136" height="88" rx="8" fill="rgba(255,255,255,.85)" stroke="#ddd" stroke-width="1.5"/>
    <g text-anchor="middle" class="tip">
      <text class="tip-text" x="512" y="841">Principal</text>
      <text class="tip-text" x="512" y="861">remaining:6402</text>
      <text class="tip-text" x="512" y="889">Years remaining:1</text>
    </g>
    <text x="588" y="708">Repayments:</text>
    <text class="stat-value" x="588" y="727">215838</text>
    <text x="588" y="758">Interest:</text>
    <text class="stat-value" x="588" y="778">115838</text>
  </svg>

  <div class="abs select-label" style="left:110px;width:141px">Repayment Type</div>
  <div class="abs select-label" style="left:289px;width:140px">Repayment Frequency</div>
  <div class="abs select" style="left:110px;width:141px"><span class="value"></span><span class="arrow"><svg width="11" height="9" viewBox="0 0 11 9"><path d="M0 0h11L5.5 9z" fill="#444"/></svg></span></div>
  <div class="abs select" style="left:289px;width:140px"><span class="value"></span><span class="arrow"><svg width="11" height="9" viewBox="0 0 11 9"><path d="M0 0h11L5.5 9z" fill="#444"/></svg></span></div>

  <footer class="abs footer"></footer>
  <div class="abs copyright">© 2016LoanHarbourGroupPtyLtd. ACN 004 218 667</div>
  <div class="abs team">Daniel K. Whitford<br>+614 1200 3400<br>Steven R. Marsh +614 1200 3455<br>Office +612 9400 1200<br>Fax +612 9400 1299</div>
</body>
</html>
```